Arborist chip truck vehicle wrap / graphics

We need a wrap design for our chipper truck that we can tie other vehicles in with. We would like to see designs incorporating our logo colors in it and potentially some gold highlights.
Id like it to say Tree DOC or tree surgeon somewhere.
a modern look is preferable
I would like the final design to be memorable and fairly simple.
Keep in mind this does not have to be a full truck wrap as we do like the white look. were looking for something interesting, use our logo as inspiration, we love it.
were highly trained and skilled and work on high end properties usually.
Updates

Target Market(s)

High end homeowners

Font styles to use
Other font styles liked:
• whatever my logo has on it

Requirements
Must have
• logo and name -
• the phrase tree Doc and /or tree surgeon
• some of our colors
• ceritifed arborist logo
• and member vbk logo
Nice to have
• maybe something saying " Keeping your trees healthy and happy"
Should not have
• too busy
• there is no back gate so dont worry about the rear of the truck

```html
<!DOCTYPE html>
<html lang="en">
<head>
<meta charset="utf-8">
<title>Oakline – Tree Surgeon Truck Side Panel</title>
<link href="https://fonts.googleapis.com/css2?family=Anton&display=swap" rel="stylesheet">
<style>
  :root {
    --leaf-green: #1d9a4b;
    --bark-brown: #5b3b1c;
    --panel-white: #ffffff;
    --canvas-grey: #e9ebec;
    --photo-tan: #c9b08c;
    --photo-bark: #8a6a45;
    --photo-moss: #9aa56d;
  }
  html, body {
    margin: 0;
    padding: 0;
    width: 1200px;
    height: 900px;
    overflow: hidden;
    background: var(--canvas-grey);
  }
  .truck-panel {
    position: relative;
    width: 1200px;
    height: 900px;
    background: var(--panel-white);
    overflow: hidden;
    font-family: "Anton", "Impact", sans-serif;
  }
  .canopy-photo {
    position: absolute;
    left: 0;
    top: 0;
    width: 1200px;
    height: 500px;
    background:
      linear-gradient(to bottom, rgba(255,255,255,0) 55%, var(--panel-white) 100%),
      linear-gradient(to right, rgba(255,255,255,0.85) 0%, rgba(255,255,255,0) 25%, rgba(255,255,255,0) 60%, rgba(255,255,255,0.9) 78%, rgba(255,255,255,0.3) 100%),
      linear-gradient(120deg, var(--photo-moss) 0%, var(--photo-tan) 35%, var(--photo-bark) 60%, var(--photo-tan) 85%, var(--photo-bark) 100%);
  }
  .brand {
    position: absolute;
    left: 40px;
    top: 40px;
    display: flex;
    align-items: center;
    gap: 12px;
    color: var(--leaf-green);
    font-size: 46px;
    letter-spacing: 2px;
    line-height: 1;
  }
  .brand-dot {
    width: 38px;
    height: 38px;
    border-radius: 50%;
    background: var(--leaf-green);
  }
  .service-title {
    position: absolute;
    right: 50px;
    top: 70px;
    margin: 0;
    text-align: right;
    color: var(--leaf-green);
    font-size: 112px;
    font-weight: 400;
    line-height: 1.02;
    letter-spacing: 1px;
  }
  .tagline {
    position: absolute;
    left: 70px;
    top: 540px;
    margin: 0;
    font-size: 122px;
    font-weight: 400;
    line-height: 1.05;
    letter-spacing: 1px;
  }
  .tagline .green { color: var(--leaf-green); }
  .tagline .brown { color: var(--bark-brown); }
  .accent-band {
    position: absolute;
    left: 0;
    bottom: 50px;
  }
  .badges {
    position: absolute;
    right: 40px;
    bottom: 40px;
    display: flex;
    gap: 20px;
  }
  .badge {
    width: 70px;
    height: 100px;
    background: var(--leaf-green);
    border: 4px solid #e6c94a;
    box-sizing: border-box;
  }
</style>
</head>
<body>
  <main class="truck-panel">
    <div class="canopy-photo" role="img" aria-label="Photo of an arborist climbing among tree branches and pine needles, fading into white"></div>

    <div class="brand">
      <span class="brand-dot"></span>
      <span class="brand-name">OAKLINE</span>
    </div>

    <h1 class="service-title">TREE<br>SURGEON</h1>

    <p class="tagline">
      <span class="green">KEEPING</span> <span class="brown">YOUR</span> <span class="green">TREES</span><br>
      <span class="brown">HEALTHY</span> <span class="green">AND</span> <span class="brown">HAPPY</span>
    </p>

    <svg class="accent-band" width="260" height="46" viewBox="0 0 260 46" aria-hidden="true">
      <polygon points="0,0 230,0 260,46 0,46" fill="var(--leaf-green)"/>
    </svg>

    <div class="badges">
      <div class="badge" aria-label="Certified arborist badge"></div>
      <div class="badge" aria-label="Member badge"></div>
    </div>
  </main>
</body>
</html>
```